Whitcombe Legal Group Promo Flyers

** I've increased the payment for this job is hopes of getting some more sophisticated design options. See feedback on current designs for guidance. I want this to be sophisticated, elegant, effective design. Please stay away from the brown/blue color palate that has been used in so many of these design options. It's not working. I'd love to see richer, deeper colors with more dimension. **

The Whitcombe Legal Group is trying to market itself as a law firm that is different than other firms. They listen to clients, meet their guidelines, provide excellent communication and will even start work for free to showcase their expertise. I need three separate flyers that will primarily be used as PDFs, but may on occasion be printed.

We're looking for a clean look.

I've attached two sample infographics that are pieces done by another company in the industry. We like that look (sizes of those are different, but the overall look is good).

Reason: Upgrading fee we'll pay and extending deadline.

Target Market(s)

Insurance companies and corporate executives who buy legal services to help them manage their book of litigation. Typical buyer is in 40s to 50s. Fairly racially diverse.

Industry/Entity Type

Communication

Requirements
Must have
• Each document will be a one-page PDF that can be easily emailed to potential clients. Must be one side only for each.

One flyer each for these three files, which are included:
Whitcombe firm by the numbers
Whitcombe firm client advantage program
Whitco firm overview

Must use firm logo. Contact information should pop.

"Topping the list" piece is an inforgraphic that should really focus on bold use of the numbers or text in blue. Mix up the page and make it fun and interesting.

Logo colors are:

Brown: R: 101 G: 50 B:27, HEX: 65321B

Grey: R:129 G: 145 B:144, HEX: 819190
Nice to have
• Firm website is very dull and uninteresting. These pieces need to pop more than past pieces.

http://www.whitcombelegalgroup.example/
Should not have
• No stock photos of people in groups (all law firms use those and they are boring and overdone).

```html
<!DOCTYPE html>
<html lang="en">
<head>
<meta charset="utf-8">
<title>Whitcombe Legal Group – Flyer</title>
<link href="https://fonts.googleapis.com/css2?family=Barlow+Semi+Condensed:wght@500;600&family=Crimson+Text:wght@400;600;700&family=Mulish:wght@300;400;700&display=swap" rel="stylesheet">
<style>
  :root {
    --page-bg: #e9ecee;
    --paper: #ffffff;
    --band-green: #5a6d66;
    --band-red: #a3271d;
    --band-red-dark: #7e1b14;
    --headline-peach: #f1d9c7;
    --brown: #65321b;
    --heading-brown: #5b2413;
    --ink: #2a2a2a;
    --text-grey: #666666;
    --rule: #b9b9b9;
    --sky-dark: #2b2d30;
  }
  * { margin: 0; padding: 0; box-sizing: border-box; }
  html, body { width: 1200px; height: 1126px; overflow: hidden; background: var(--page-bg); }
  .stage { position: relative; width: 1200px; height: 1126px; }
  .flyer {
    position: absolute; left: 181px; top: 20px;
    width: 670px; height: 868px;
    transform: scale(1.25); transform-origin: top left;
    background: linear-gradient(#ffffff 260px, #f1f1f1 520px, #ffffff 640px);
    overflow: hidden;
    font-family: "Mulish", sans-serif;
    box-shadow: 0 2px 10px rgba(0,0,0,.15);
  }
  .header { position: absolute; left: 0; top: 0; width: 670px; height: 115px; background: var(--paper); }
  .logo {
    position: absolute; left: 28px; top: 32px;
    font-family: "Crimson Text", serif; font-weight: 400;
    color: var(--brown); font-size: 25px; line-height: 26px;
  }
  .hero { position: absolute; left: 0; top: 115px; width: 670px; height: 105px; background: var(--band-green); }
  .hero h1 {
    position: absolute; left: 32px; top: 16px;
    font-family: "Barlow Semi Condensed", sans-serif; font-weight: 500;
    font-size: 24px; color: var(--headline-peach); letter-spacing: .2px;
  }
  .hero p {
    position: absolute; left: 32px; top: 50px; width: 610px;
    font-family: "Barlow Semi Condensed", sans-serif; font-weight: 600;
    font-size: 14.6px; line-height: 21px; color: #fff;
  }
  .contact-bar { position: absolute; left: 0; top: 220px; width: 670px; height: 28px; }
  .contact-bar svg { position: absolute; left: 0; top: 0; }
  .contact-bar .web, .contact-bar .phone {
    position: absolute; top: 5px;
    font-family: "Crimson Text", serif; font-weight: 700; font-size: 13px; color: #fff;
  }
  .contact-bar .web { left: 32px; }
  .contact-bar .phone { left: 272px; }
  .contact-bar .names {
    position: absolute; left: 358px; top: 8px;
    font-family: "Barlow Semi Condensed", sans-serif; font-size: 10.5px; color: #f4dcd4;
  }
  .contact-bar .names b { color: #fff; font-weight: 600; }

  .skyline {
    position: absolute; left: 0; top: 590px; width: 670px; height: 278px; z-index: 0;
    background:
      linear-gradient(rgba(255,255,255,1) 0px, rgba(255,255,255,.85) 100px, rgba(255,255,255,0) 170px),
      linear-gradient(90deg, #6a6d71 0%, #c3c6c9 28%, #4a4c50 45%, #b9bcbf 62%, #4e5054 78%, #aeb1b4 100%);
  }
  .skyline::after {
    content: ""; position: absolute; left: 0; bottom: 0; width: 100%; height: 80px;
    background: linear-gradient(rgba(43,45,48,0), var(--sky-dark));
  }

  .practice { position: absolute; left: 0; top: 272px; width: 215px; z-index: 1; }
  .practice h2 {
    margin-left: 31px; margin-bottom: 18px;
    font-family: "Barlow Semi Condensed", sans-serif; font-weight: 500; font-size: 14px; color: #555;
  }
  .area { padding: 0 0 9px 31px; border-bottom: 1px solid var(--rule); margin-bottom: 9px; }
  .area h3 {
    font-family: "Mulish", sans-serif; font-weight: 700; font-size: 11px; color: var(--ink);
    display: flex; align-items: center; gap: 4px;
  }
  .area h3::before { content: ""; width: 5px; height: 5px; background: var(--band-green); }
  .area p { font-size: 10.2px; line-height: 16px; color: #333; margin-top: 2px; letter-spacing: -.15px; white-space: normal; }
  .area p.one-line { white-space: nowrap; }

  .features { position: absolute; left: 272px; top: 276px; width: 368px; z-index: 1; }
  .feature { margin-bottom: 22px; }
  .feature h2 {
    font-family: "Barlow Semi Condensed", sans-serif; font-weight: 600;
    font-size: 14.5px; color: var(--heading-brown); letter-spacing: .2px; line-height: 16px;
  }
  .feature p { font-size: 9.3px; line-height: 13.4px; color: var(--text-grey); font-weight: 300; }
  .feature p strong { font-weight: 700; color: var(--ink); }
</style>
</head>
<body>
<div class="stage">
  <article class="flyer">
    <div class="skyline" role="img" aria-label="Black and white photograph of a city skyline at night"></div>

    <header class="header">
      <div class="logo">Whitcombe<br>Legal Group</div>
    </header>

    <section class="hero">
      <h1>We Protect Your Business Interests.</h1>
      <p>We help businesses, professionals and entrepreneurs win their business lawsuits, often in the middle of an emergency. Our Chicago Law Firm is successful in helping clients resolve problems and achieve goals.</p>
    </section>

    <div class="contact-bar">
      <svg width="670" height="28" viewBox="0 0 670 28" aria-hidden="true">
        <rect x="0" y="0" width="670" height="28" fill="var(--band-red)"/>
        <rect x="0" y="25" width="670" height="3" fill="var(--band-red-dark)"/>
        <polygon points="520,0 542,17 670,17 670,0" fill="var(--band-green)"/>
      </svg>
      <span class="web">www.whitcombelegalgroup.example</span>
      <span class="phone">855-555-0142</span>
      <span class="names">Contact <b>Tom Whitcombe</b> or <b>Dan Halvorsen</b></span>
    </div>

    <aside class="practice">
      <h2>Practice Areas</h2>
      <div class="area"><h3>Insurance</h3><p>coverage, defense, subrogation, risk managing, program administration</p></div>
      <div class="area"><h3>Professional Liability</h3><p class="one-line">attorneys, accountants, D &amp; O, E &amp; O, EPL</p></div>
      <div class="area"><h3>Business Litigation</h3><p>emergencies, injunctions, contract, partners, shareholders, employees, property, trade secrets, restrictive covenants, banking, finance</p></div>
      <div class="area"><h3>Construction</h3></div>
      <div class="area"><h3>Commercial Transportation</h3></div>
    </aside>

    <main class="features">
      <section class="feature">
        <h2>CLIENTS COME FIRST</h2>
        <p><strong>Our extremely well-credentialed attorneys</strong> know that clients want more than legal expertise — they want partners who understand that communication and process during the management of a case are just as important as the outcome. They want advice and guidance. They want a true business partner.</p>
      </section>
      <section class="feature">
        <h2>GREAT OUTCOMES, GREAT PROCESS, GREAT COMMUNICATION</h2>
        <p><strong>A good attorney will get you the desired outcome on a case.</strong> A great attorney will do the same while following your process and keeping your informed along the way — all while being mindful of the established budget. We work closely with our clients to understand their litigation management guidelines and we ensure that we follow them. We know that our clients have their own internal reporting structures and timeframes and we strive to provide the work product and communication so those reporting requirements can be met.</p>
      </section>
      <section class="feature">
        <h2>METRICS THAT MATTER</h2>
        <p><strong>Providing excellent legal counsel today also means</strong> being able to provide clients with the data they need to evaluate performance. While we’re managing the details of each case, we’re also keeping track of the big picture so we can report metrics back to our clients. Cycle time, cost, quality and predictability are just some of the metrics we track. We work with each client to ensure we have the data they desire. We understand and embrace the importance of business process</p>
      </section>
      <section class="feature">
        <h2>EXPERTISE NO ONE ELSE HAS</h2>
        <p><strong>Our attorneys bring unique expertise to managing our clients’ litigation.</strong> For example, we excel at transportation and construction cases because one of our partners, Dan Halvorsen, ran a trucking company, and then was responsible for maintaining mining machines on the Deep Tunnel project in Chicago. Another partner, Tom Whitcombe, has deep knowledge of emergency litigation. We’ve literally been in the trenches sharing your business &amp; life experiences. Each of our attorneys brings unique perspectives to each of the Firm’s practice areas</p>
      </section>
    </main>
  </article>
</div>
</body>
</html>
```